Tanwick Services Website Design

We have most content but require a professional design. We have a logo already and will need it utilized along with several of the photos from the attached documentation.
First page should have our mission and Vision and the synapsis provided in the word document. Visitors will be prompted to select from one of our 3 divisions from this page.
Each division will have the same list of tabs : About, Services, Safety, Careers and Contact.
Photos on each divisions page should be representative of the divisions offerings. The word doc attached contains the requested content and we are open to edits that would complement and fill the website.
I like the Morvalix site www.morvalix-demo.net - they are our competition so cant be modeled directly after this.
Please include prompts to request quote at each service page. align the format of the geotechnical page to the other 2 divisions.
I used chat gpt for some of the content so will need it optimized for SCO.

```html
<!DOCTYPE html>
<html lang="en">
<head>
<meta charset="utf-8">
<title>Tanwick Services</title>
<link href="https://fonts.googleapis.com/css2?family=Lexend:wght@400;500;600;700;800&family=Poppins:wght@400;500;600&display=swap" rel="stylesheet">
<style>
:root{
  --red:#e5242a;
  --black:#000;
  --ink:#1a1a1a;
  --white:#fff;
  --muted:#8a8a8a;
  --footer:#1c1c1c;
}
*{margin:0;padding:0;box-sizing:border-box}
html,body{width:1200px;height:3599px;overflow:hidden;background:var(--white)}
body{position:relative;font-family:"Poppins",sans-serif;color:var(--ink)}
.abs{position:absolute}
.head{font-family:"Lexend",sans-serif;font-weight:400}
.accent{color:var(--red);font-weight:600}
.section-title{position:absolute;left:0;width:1200px;text-align:center;font-family:"Lexend",sans-serif;font-size:29px}

/* hero */
.hero{left:0;top:0;width:1200px;height:529px;overflow:hidden}
.hero-photo{position:absolute;inset:0;background:linear-gradient(180deg,#4d5446 0%,#5e5f53 35%,#3a3a33 70%,#2e2b28 100%)}
.hero-shade{position:absolute;inset:0;background:linear-gradient(90deg,rgba(0,0,0,.45),rgba(0,0,0,.1) 60%,rgba(0,0,0,.2))}
.brand{font-family:"Lexend",sans-serif;font-weight:700;color:var(--red);font-size:30px;letter-spacing:1px}
.nav{top:32px;font-size:11px;color:var(--white);font-weight:500}
.nav a{position:absolute;color:var(--white);text-decoration:none;white-space:nowrap}
.nav .active{color:var(--red)}
.quote-btn{position:absolute;left:1000px;top:17px;width:125px;height:36px;border:1.5px solid var(--white);border-radius:18px;text-align:center;line-height:33px;font-size:11px}
.hero-title{left:138px;top:212px;color:var(--white);font-family:"Lexend",sans-serif;font-size:37px;font-weight:600}
.hero-sub{left:138px;top:252px;color:var(--white);font-family:"Lexend",sans-serif;font-size:29px;line-height:39px;font-weight:400}
.pill{position:absolute;background:var(--red);color:var(--white);border-radius:18px;text-align:center;font-size:10px;font-weight:500}
.slider-btn{position:absolute;top:490px;width:36px;height:36px;background:var(--white);text-align:center;line-height:34px;font-size:14px;color:var(--ink)}

/* services */
.svc{position:absolute;top:671px;height:166px;background:var(--white);box-shadow:0 4px 18px rgba(0,0,0,.09);text-align:center}
.svc svg{margin-top:30px}
.svc p{position:absolute;left:0;right:0;top:113px;font-size:12px;font-weight:500}
.svc.on{background:var(--red);color:var(--white)}
.outline-btn{position:absolute;height:36px;border:1.5px solid var(--red);border-radius:18px;color:var(--red);text-align:center;line-height:33px;font-size:10px;font-weight:500}

/* vision / mission */
.dark{background:var(--black)}
.vision-title{top:1082px;color:var(--white)}
.vision-text{left:0;width:1200px;top:1136px;text-align:center;color:var(--white);font-size:13.5px;line-height:23px}
.mission-title{left:138px;top:1298px;color:var(--white);font-family:"Lexend",sans-serif;font-size:29px}
.mission-text{left:138px;top:1352px;width:460px;color:var(--white);font-size:13px;line-height:24.8px}
.photo{position:absolute;border-radius:3px}

/* division */
.div-label{position:absolute;font-size:12px;font-weight:500;text-align:center;width:200px}

/* careers */
.careers{left:0;top:2297px;width:1200px;height:291px;background:var(--red)}
.careers h3{position:absolute;left:138px;top:52px;color:var(--white);font-family:"Lexend",sans-serif;font-size:29px;font-weight:400}
.careers p{position:absolute;left:138px;top:110px;width:470px;color:var(--white);font-size:17px;line-height:22px}
.careers .apply{position:absolute;left:138px;top:202px;width:125px;height:36px;background:var(--white);color:var(--red);border-radius:18px;text-align:center;line-height:36px;font-size:10px;font-weight:600}
.careers .wordmark{position:absolute;left:700px;top:108px;color:var(--white);font-family:"Lexend",sans-serif;font-weight:800;font-size:70px;letter-spacing:6px}

/* articles */
.art-title{position:absolute;font-size:13px;line-height:18px}
.art-small{position:absolute;font-size:9px;line-height:15px;color:var(--muted)}

/* footer */
.footer{left:0;top:3223px;width:1200px;height:376px;background:linear-gradient(160deg,#262626,#141414 60%,#222)}
.f-head{position:absolute;color:var(--white);font-size:12px;font-weight:500}
.f-link{position:absolute;color:var(--white);font-size:9.5px}
.social{position:absolute;top:3386px;width:22px;height:22px;border-radius:50%;background:#6b6b6b}
</style>
</head>
<body>

<!-- hero -->
<header class="abs hero">
  <div class="hero-photo" role="img" aria-label="Photo of a white aerial lift truck parked in a field beside evergreen trees"></div>
  <div class="hero-shade"></div>
  <div class="abs brand" style="left:75px;top:18px">TANWICK</div>
  <nav class="abs nav" style="left:0;top:32px;width:1200px">
    <a class="active" style="left:515px">Home</a>
    <a style="left:560px">About Us</a>
    <a style="left:636px">Services</a>
    <a style="left:712px">Divisions</a>
    <a style="left:785px">Contact Us</a>
    <a style="left:866px">
      <svg width="10" height="10" viewBox="0 0 24 24" style="vertical-align:-1px"><path fill="#fff" d="M6.6 10.8a15 15 0 0 0 6.6 6.6l2.2-2.2c.3-.3.7-.4 1-.2 1.1.4 2.3.6 3.6.6.6 0 1 .4 1 1V20c0 .6-.4 1-1 1A17 17 0 0 1 3 4c0-.6.4-1 1-1h3.5c.6 0 1 .4 1 1 0 1.3.2 2.5.6 3.6.1.3 0 .7-.2 1z"/></svg>
      (555) 210-4870</a>
    <span class="quote-btn" style="top:-15px">Request a Quote</span>
  </nav>
  <h1 class="abs hero-title">Tanwick</h1>
  <p class="abs hero-sub">Your Partner in Wind Turbine<br>Performance!</p>
  <span class="pill" style="left:138px;top:358px;width:125px;height:36px;line-height:36px">Our Services</span>
  <svg class="abs" style="left:594px;top:462px" width="12" height="34" viewBox="0 0 12 34"><path d="M6 0v31M2 27l4 5 4-5" stroke="#fff" stroke-width="1.3" fill="none"/></svg>
  <span class="slider-btn" style="left:985px">&#8249;</span>
  <span class="slider-btn" style="left:1028px">&#8250;</span>
</header>

<!-- services -->
<h2 class="section-title" style="top:602px"><span class="head">Tanwick</span> <span class="accent">Services</span></h2>

<div class="svc" style="left:75px;width:190px">
  <svg width="64" height="64" viewBox="0 0 64 64" fill="none" stroke="#1a1a1a" stroke-width="2.5"><path d="M32 6l18 8v14c0 12-8 20-18 24-10-4-18-12-18-24V14z" fill="#e5242a"/><circle cx="32" cy="28" r="7" fill="#fff"/><path d="M8 50h48M14 56h36"/></svg>
  <p>Delivering safe</p>
</div>
<div class="svc on" style="left:291px;width:190px">
  <svg width="64" height="64" viewBox="0 0 64 64" fill="none" stroke="#fff" stroke-width="2.5"><rect x="8" y="22" width="22" height="22"/><path d="M30 30l16-22 6 4-14 20M46 8v16"/><path d="M4 48h56M4 56h56"/></svg>
  <p>Oil&amp;Gas</p>
</div>
<div class="svc" style="left:507px;width:187px">
  <svg width="64" height="64" viewBox="0 0 64 64" fill="none" stroke="#1a1a1a" stroke-width="2.5"><path d="M20 58V10h30M20 16h24v8"/><rect x="30" y="32" width="24" height="26" fill="#e5242a"/><path d="M30 45h24M42 32v26"/></svg>
  <p>Construction</p>
</div>
<div class="svc" style="left:721px;width:188px">
  <svg width="64" height="64" viewBox="0 0 64 64" fill="none" stroke="#1a1a1a" stroke-width="2.5"><path d="M32 4L20 58M32 4l12 54M14 18h36M10 30h44M24 40l16 10M40 40L24 50"/><circle cx="14" cy="22" r="3" fill="#e5242a"/><circle cx="50" cy="22" r="3" fill="#e5242a"/></svg>
  <p>Utility</p>
</div>
<div class="svc" style="left:935px;width:190px">
  <svg width="64" height="64" viewBox="0 0 64 64" fill="none" stroke="#1a1a1a" stroke-width="2.5"><path d="M32 26L14 8M32 26l22-12M32 26l2 22M32 26v32M24 58h16"/><circle cx="32" cy="26" r="4" fill="#e5242a"/></svg>
  <p>Renewable energy</p>
</div>

<span class="outline-btn" style="left:538px;top:869px;width:125px">Explore More</span>

<!-- vision & mission -->
<div class="abs dark" style="left:0;top:1011px;width:1200px;height:731px"></div>
<div class="abs dark" style="left:1125px;top:980px;width:75px;height:794px"></div>
<div class="abs dark" style="left:0;top:1742px;width:75px;height:32px"></div>

<h2 class="section-title vision-title"><span class="head">Our</span> <span class="accent">Vision</span></h2>
<p class="abs vision-text">To be the leading provider of aerial access, geotechnical drilling, and service solutions, setting the<br>standard for excellence in safety, efficiency, and environmental stewardship.</p>

<h2 class="abs mission-title">Our <span class="accent">Mission</span></h2>
<p class="abs mission-text">At Tanwick, our mission is to deliver unparalleled<br>aerial access, geotechnical drilling, and service and maintenance<br>solutions, consistently exceeding our clients' expectations.<br>We strive to achieve this by investing in cutting-edge<br>technology, fostering a culture of safety and continuous<br>improvement, and prioritizing environmental sustainability.<br>Through collaboration, integrity, and dedication,<br>we aim to contribute to the success of our clients while<br>maintaining the highest standards of quality and<br>professionalism.</p>

<div class="photo" style="left:661px;top:1227px;width:412px;height:440px;background:linear-gradient(180deg,#b9c0c6 0%,#cfd3d6 45%,#8f8c86 62%,#6f6b64 100%)" role="img" aria-label="Photo of two white boom trucks parked on a gravel lot under an overcast sky"></div>

<!-- select division -->
<h2 class="section-title" style="top:1817px"><span class="head">Select</span> <span class="accent">Division</span></h2>

<svg class="abs" style="left:0;top:1890px" width="1200" height="345" viewBox="0 1890 1200 345">
  <defs><clipPath id="dome"><path d="M210 2221 Q600 1760 990 2221 Z"/></clipPath></defs>
  <path d="M201 2221 Q600 1740 999 2221" fill="none" stroke="#e5242a" stroke-width="1.5"/>
  <g clip-path="url(#dome)">
    <rect x="200" y="1900" width="800" height="330" fill="url(#ground)"/>
  </g>
  <linearGradient id="ground" x1="0" y1="0" x2="0" y2="1"><stop offset="0" stop-color="#9a8a76"/><stop offset=".5" stop-color="#7a6c5e"/><stop offset="1" stop-color="#3f3a35"/></linearGradient>
  <rect x="540" y="2010" width="120" height="170" fill="#5b7fae" opacity=".55" role="img" aria-label="Photo of a blue drilling truck on a dirt road"/>
  <text x="600" y="2218" text-anchor="middle" fill="#fff" font-family="Lexend, sans-serif" font-weight="800" font-size="56" letter-spacing="8">TANWICK</text>
  <g>
    <circle cx="374" cy="2059" r="45" fill="#000" stroke="#fff" stroke-width="4"/>
    <path d="M354 2070h40M358 2070v-14h14v14M372 2060l14-18" stroke="#fff" stroke-width="3" fill="none"/>
    <circle cx="362" cy="2074" r="3" fill="#e5242a"/><circle cx="388" cy="2074" r="3" fill="#e5242a"/>
    <circle cx="600" cy="1978" r="45" fill="#e5242a" stroke="#fff" stroke-width="4"/>
    <path d="M588 1998v-34h6v34M594 1972l16 26M584 1998h32" stroke="#fff" stroke-width="3" fill="none"/>
    <circle cx="825" cy="2059" r="45" fill="#000" stroke="#fff" stroke-width="4"/>
    <circle cx="825" cy="2059" r="20" fill="#e5242a"/>
    <path d="M829 2045l-10 16h9l-4 13 10-17h-9z" fill="#fff"/>
  </g>
</svg>
<div class="div-label" style="left:500px;top:1899px">Geotechnical Drilling</div>
<div class="div-label" style="left:274px;top:1979px">Aerial Access</div>
<div class="div-label" style="left:725px;top:1960px;line-height:15px">Renewable Energy<br>Services</div>

<!-- careers -->
<section class="abs careers">
  <h3>Careers</h3>
  <p>We are always looking for skilled blade technicians, wind turbine maintenance technicians to join our team.</p>
  <span class="apply">Apply Now</span>
  <div class="wordmark">TANWICK</div>
</section>

<!-- articles -->
<h2 class="section-title" style="top:2664px"><span class="head">Recent</span> <span class="accent">Articles</span></h2>

<div class="photo" style="left:138px;top:2757px;width:244px;height:217px;background:linear-gradient(180deg,#a9c6e4,#6f8fb0 60%,#3d5775)" role="img" aria-label="Photo looking up at glass office towers"></div>
<p class="art-title" style="left:138px;top:2985px;width:244px">There are many variations of<br>passages of lorem Ipsum<br>available</p>

<div class="photo" style="left:406px;top:2725px;width:389px;height:279px;background:linear-gradient(180deg,#c9cfa7,#e8e4d8 45%,#a88258 100%)" role="img" aria-label="Photo of architectural plans, a model house and a hard hat on a desk"></div>
<p class="art-title" style="left:406px;top:3024px;width:389px">Contrary to popular belief</p>
<p class="art-small" style="left:406px;top:3047px;width:389px">There are many variations of passages of lorem ipsum available,<br>but the majority.</p>

<div class="photo" style="left:820px;top:2757px;width:244px;height:217px;background:linear-gradient(180deg,#3a3a3e,#9aa6b3 40%,#8b8d90 70%,#4a4a4c)" role="img" aria-label="Photo of a highway overpass framed by a concrete arch"></div>
<p class="art-title" style="left:820px;top:2985px;width:244px">There are many variations of<br>passages of lorem Ipsum<br>available</p>

<span class="outline-btn" style="left:551px;top:3113px;width:125px">View All</span>

<!-- footer -->
<footer class="abs footer" role="img" aria-label="Dark photo of a service truck at a work site behind the footer"></footer>
<div class="abs" style="left:138px;top:3348px;color:#fff;font-family:'Lexend',sans-serif;font-weight:700;font-size:27px;letter-spacing:3px">TANWICK</div>

<div class="f-head" style="left:406px;top:3343px">Contact Us</div>
<svg class="abs" style="left:406px;top:3387px" width="11" height="11" viewBox="0 0 24 24"><path fill="#e5242a" d="M6.6 10.8a15 15 0 0 0 6.6 6.6l2.2-2.2c.3-.3.7-.4 1-.2 1.1.4 2.3.6 3.6.6.6 0 1 .4 1 1V20c0 .6-.4 1-1 1A17 17 0 0 1 3 4c0-.6.4-1 1-1h3.5c.6 0 1 .4 1 1 0 1.3.2 2.5.6 3.6.1.3 0 .7-.2 1z"/></svg>
<div class="f-link" style="left:425px;top:3384px;font-size:13px">(555) 210-4870</div>
<svg class="abs" style="left:406px;top:3420px" width="11" height="11" viewBox="0 0 24 24"><circle cx="12" cy="7" r="5" fill="#e5242a"/><path d="M3 22c0-6 4-9 9-9s9 3 9 9z" fill="#e5242a"/></svg>
<div class="f-link" style="left:425px;top:3418px">info@tanwickservices.example</div>
<svg class="abs" style="left:406px;top:3449px" width="11" height="13" viewBox="0 0 24 28"><path fill="#e5242a" d="M12 0a9 9 0 0 0-9 9c0 7 9 19 9 19s9-12 9-19a9 9 0 0 0-9-9zm0 12a3 3 0 1 1 0-6 3 3 0 0 1 0 6z"/></svg>
<div class="f-link" style="left:425px;top:3447px;font-size:8.5px;line-height:15px">118 Ridge Road Calder Falls<br>AB T0X-1B0</div>

<div class="f-head" style="left:663px;top:3343px">Quick Links</div>
<div class="f-link" style="left:663px;top:3384px">Home</div>
<div class="f-link" style="left:663px;top:3406px">About Us</div>
<div class="f-link" style="left:663px;top:3428px">Services</div>
<div class="f-link" style="left:663px;top:3451px">Divisions</div>
<div class="f-link" style="left:663px;top:3473px">Contact Us</div>
<div class="f-link" style="left:736px;top:3384px">Careers</div>
<div class="f-link" style="left:736px;top:3406px">News</div>
<div class="f-link" style="left:736px;top:3428px">Term &amp; Conditions</div>
<div class="f-link" style="left:736px;top:3451px">Privacy Policy</div>

<div class="f-head" style="left:885px;top:3343px">Follow Us</div>
<span class="social" style="left:885px"></span>
<span class="social" style="left:915px;background:var(--red)"></span>
<span class="social" style="left:946px"></span>
<span class="social" style="left:977px"></span>

<svg class="abs" style="left:1123px;top:3368px" width="16" height="18" viewBox="0 0 16 18"><path d="M8 0l8 18-8-5-8 5z" fill="#e5242a"/></svg>

<div class="abs" style="left:75px;top:3535px;width:1050px;height:1px;background:rgba(255,255,255,.15)"></div>
<div class="abs" style="left:0;top:3563px;width:1200px;text-align:center;color:#fff;font-size:9px">© 2024 <span style="color:var(--red)">Tanwick</span>. All Rights Reserved</div>

</body>
</html>
```